Brightwave Partners, Inc. Website redesign

Revamp the website, it is old and outdated. www.brightwavepartnersinc.example

Target Market(s)

Information Technology Consulting and Staffing

Coding

Coded - Design and coding required

Number of Pages Required

5+ page

Colors

Designer to choose colors to be used in the design.

Requirements
Must have
• Outlined text boxes just like from the Tolvane.us site. A clean look

```html
<!DOCTYPE html>
<html lang="en">
<head>
<meta charset="utf-8">
<title>Brightwave Partners, Inc.</title>
<link href="https://fonts.googleapis.com/css2?family=Jost:wght@400;500&family=Montserrat:wght@600;700;800&display=swap" rel="stylesheet">
<style>
:root{
  --red:#a51d36;
  --red-dark:#8c1329;
  --ink:#231f20;
  --text:#333;
  --muted:#555;
  --light:#efefef;
  --white:#fff;
  --footer:#262626;
}
*{box-sizing:border-box;margin:0;padding:0}
html,body{width:1200px;height:3337px;overflow:hidden}
body{font-family:"Jost",sans-serif;color:var(--text);background:var(--white);position:relative}
.head-font{font-family:"Montserrat",sans-serif}
a{color:inherit;text-decoration:none}

.topbar{height:28px;background:var(--red);color:var(--white);font-size:12px;display:flex;align-items:center;padding:0 140px;gap:28px}
.topbar .item{display:flex;align-items:center;gap:8px}
.socials{margin-left:auto;display:flex;gap:8px}
.socials span{width:16px;height:16px;border-radius:50%;background:var(--white)}

.header{height:76px;display:flex;align-items:center;padding:0 140px}
.brand{display:flex;align-items:center;gap:10px;font-family:"Montserrat",sans-serif;font-weight:800;font-size:20px;color:var(--ink);letter-spacing:.5px}
.brand .mark{width:22px;height:22px;background:var(--red)}
.nav{margin-left:auto;display:flex;gap:31px;font-family:"Montserrat",sans-serif;font-weight:600;font-size:12px;color:var(--ink)}
.nav .active{color:var(--red)}
.nav-search{margin-left:22px;padding-left:18px;border-left:1px solid #ccc;height:18px;display:flex;align-items:center}

.hero{position:relative;height:541px;background:linear-gradient(100deg,#6d6c66 0%,#b8b6ae 30%,#d9d6ce 55%,#c6c4bd 80%,#9a978f 100%)}
.hero-copy{position:absolute;left:733px;top:206px;width:322px;text-align:center;color:var(--white);text-shadow:0 2px 4px rgba(0,0,0,.4)}
.hero-copy h1{font-family:"Montserrat",sans-serif;font-weight:800;font-size:30px;letter-spacing:1px}
.hero-copy p{font-size:15px;margin-top:12px}
.btn{display:inline-flex;align-items:center;gap:8px;background:var(--red);color:var(--white);font-size:15px;padding:5px 10px;box-shadow:3px 3px 4px rgba(0,0,0,.3)}
.btn .sq{width:14px;height:14px;border:2px solid var(--white)}
.hero-copy .btn{margin-top:18px;text-shadow:none;font-size:16px;padding:6px 10px}
.hero-notch{position:absolute;left:0;bottom:-1px}

.kicker{color:var(--red);font-size:14px;text-align:center;text-transform:uppercase}
.section-title{font-family:"Montserrat",sans-serif;font-weight:800;font-size:28px;text-align:center;color:var(--ink);letter-spacing:1px}

.about{height:446px;padding-top:90px;text-align:center}
.about .section-title{margin-top:2px}
.about .copy{width:870px;margin:28px auto 0;font-size:11.5px;line-height:22px;color:var(--ink)}
.about .copy p+p{margin-top:8px}
.about .btn{margin-top:34px}

.services{height:565px;background:linear-gradient(90deg,#2b2b2b,#4a4a48 50%,#3a3a38);color:var(--white);padding-top:70px;position:relative}
.services .kicker{color:var(--white)}
.services .section-title{color:var(--white)}
.cards{position:absolute;top:166px;left:158px;display:flex;gap:14px}
.svc-card{width:210px;height:328px;background:var(--white);border-top:3px solid var(--red);color:var(--ink);padding:0 0}
.svc-card h3{font-family:"Montserrat",sans-serif;font-weight:700;font-size:12.5px;height:44px;display:flex;align-items:center;padding:0 9px}
.svc-card .photo{height:146px;background:linear-gradient(135deg,#6e7a86,#c9cdd2)}
.svc-card .photo.dark{background:linear-gradient(135deg,#2a2e35,#6f6358)}
.svc-card .photo.blue{background:linear-gradient(135deg,#1f3148,#5a7a99)}
.svc-card p{font-size:10.5px;line-height:13px;padding:14px 8px 0;height:66px;color:#444}
.svc-card .btn{margin-left:8px;font-size:11px;padding:6px 26px;box-shadow:none}
.arrow-btn{position:absolute;top:313px;width:32px;height:32px;border-radius:50%;background:#bdbdbd;display:flex;align-items:center;justify-content:center}

.strategy{height:612px;background:var(--light);padding-top:78px;text-align:center}
.strategy .section-title{margin-top:0}
.strategy .copy{width:760px;margin:30px auto 0;font-size:11.5px;line-height:15px;color:var(--ink)}
.strategy .copy p+p{margin-top:16px}
.strategy .lead{margin-top:14px;font-size:12.5px}
.diagram{display:block;margin-top:18px}

.blog{height:622px;padding-top:78px;position:relative}
.blog .section-title{margin-top:0}
.posts{position:absolute;top:159px;left:141px;display:flex;gap:35px}
.post{width:283px;height:389px;background:var(--white);border-top:2px solid var(--red);box-shadow:0 1px 5px rgba(0,0,0,.25);text-align:center;position:relative}
.post .photo{height:176px;background:linear-gradient(135deg,#5a4236,#c9c2b8)}
.post .photo.cool{background:linear-gradient(135deg,#9aa7b3,#e3e6ea)}
.post .photo.screen{background:linear-gradient(135deg,#3b6fa0,#9ec6e6)}
.date{position:absolute;left:0;top:0;background:var(--ink);color:var(--white)}
.date .d{display:block;background:var(--red);font-size:24px;line-height:32px;width:54px}
.date .m{display:block;font-size:12px;line-height:18px;width:54px}
.post h4{font-weight:400;font-size:16px;line-height:23px;margin-top:20px;color:var(--ink)}
.post p{font-size:12px;line-height:19px;margin-top:20px;color:#444}
.post .btn{margin-top:16px;font-size:12px;padding:4px 10px;box-shadow:none}
.chev{position:absolute;top:2590px}

.footer{position:absolute;left:0;top:2880px;width:1200px;height:457px}
.footer-body{position:absolute;top:100px;left:0;width:1200px;height:322px;background:var(--footer);color:#ddd}
.fcol{position:absolute;top:0}
.fcol h5{font-weight:500;font-size:17px;color:var(--white);padding-bottom:10px;border-bottom:1px solid #777;display:inline-block;padding-right:30px}
.links{list-style:none;margin-top:14px;font-size:11.5px}
.links li{line-height:29px}
.links li::before{content:"›";margin-right:6px;color:#999}
.contact-row{display:flex;gap:10px;align-items:flex-start;font-size:13px;line-height:19px;margin-top:14px}
.ring{width:30px;height:30px;border:2px solid var(--white);border-radius:50%;flex:none;display:flex;align-items:center;justify-content:center}
.footer .brand{color:var(--white)}
.fabout{font-size:11.5px;line-height:18px;margin-top:22px;width:260px}
.vline{position:absolute;top:40px;width:1px;height:180px;background:#3a3a3a}
.bottombar{position:absolute;left:0;bottom:0;width:1200px;height:35px;background:var(--red);color:var(--white);font-size:12px;display:flex;align-items:center;padding:0 145px}
</style>
</head>
<body>

<div class="topbar">
  <div class="item">
    <svg width="13" height="13" viewBox="0 0 24 24"><path fill="#fff" d="M6.6 10.8a15 15 0 0 0 6.6 6.6l2.2-2.2a1 1 0 0 1 1-.25 11.4 11.4 0 0 0 3.6.57 1 1 0 0 1 1 1V20a1 1 0 0 1-1 1A17 17 0 0 1 3 4a1 1 0 0 1 1-1h3.5a1 1 0 0 1 1 1c0 1.25.2 2.45.57 3.57a1 1 0 0 1-.25 1z"/></svg>
    555.010.2040
  </div>
  <div class="item">
    <svg width="16" height="11" viewBox="0 0 16 11"><rect x=".5" y=".5" width="15" height="10" fill="none" stroke="#fff"/><path d="M.5.5 8 6l7.5-5.5" fill="none" stroke="#fff"/></svg>
    inquiry@brightwavepartners.example
  </div>
  <div class="socials"><span></span><span></span><span></span><span></span></div>
</div>

<header class="header">
  <div class="brand"><span class="mark"></span>Brightwave Partners</div>
  <nav class="nav">
    <a class="active">HOME</a><a>ABOUT US</a><a>SERVICES</a><a>STRATEGY</a><a>IT NEWS</a><a>CONTACT US</a>
  </nav>
  <div class="nav-search">
    <svg width="14" height="14" viewBox="0 0 14 14"><circle cx="6" cy="6" r="4.5" fill="none" stroke="#a51d36" stroke-width="1.5"/><path d="M9.5 9.5 13 13" stroke="#a51d36" stroke-width="1.5"/></svg>
  </div>
</header>

<section class="hero" role="img" aria-label="Photo of smiling consultants reviewing documents in a bright office">
  <div class="hero-copy">
    <h1>MEET OUR EXPERTS</h1>
    <p>We stand behind your Success.</p>
    <a class="btn"><span class="sq"></span>Contact Us Today</a>
  </div>
  <svg class="hero-notch" width="1200" height="40" viewBox="0 0 1200 40">
    <path d="M530 40 C560 40 570 8 600 8 C630 8 640 40 670 40 Z" fill="#fff"/>
    <path d="M600 16v22M594 32l6 6 6-6" fill="none" stroke="#a51d36" stroke-width="1.3"/>
  </svg>
</section>

<section class="about">
  <div class="kicker">About</div>
  <h2 class="section-title">BRIGHTWAVE PARTNERS INC.</h2>
  <div class="copy">
    <p>Brightwave Partners, Inc. is an 8(a) innovative and rapidly growing full-service IT consulting firm. We provide our clients with cutting-edge technologies and the know-how to apply them to their individual business models.</p>
    <p>For over 20 + years, we have been providing reliable IT solutions to businesses in the Washington, DC Metro area and beyond. Our comprehensive services provide clients with unique technology solutions that are customized to meet the specific demands of their business.</p>
    <p>Look to our experts for strategic IT guidance, management and services that allows you to take your mind off technology and concentrate on your core area of business. Brightwave Partners, Inc. provides cost-efficient solutions that simply make good sense.</p>
  </div>
  <a class="btn"><span class="sq"></span>Read More</a>
</section>

<section class="services" role="region" aria-label="Services, backdrop photo of an office team">
  <div class="kicker">Services</div>
  <h2 class="section-title">WHAT WE DO</h2>
  <div class="arrow-btn" style="left:86px"><svg width="10" height="10"><path d="M7 1 2 5l5 4z" fill="#333"/></svg></div>
  <div class="arrow-btn" style="left:1092px;top:318px"><svg width="10" height="10"><path d="M3 1l5 4-5 4z" fill="#333"/></svg></div>
  <div class="cards">
    <article class="svc-card">
      <h3>Hardware / Software Sales</h3>
      <div class="photo" role="img" aria-label="Photo of a team meeting in a conference room"></div>
      <p>We have access to multiple distributor partners throughout North America, as well as Elite Partner Status with many…</p>
      <a class="btn">Read More</a>
    </article>
    <article class="svc-card">
      <h3>Professional Services</h3>
      <div class="photo dark" role="img" aria-label="Photo of a technician working at a server rack"></div>
      <p>Our team provides experienced leadership and guidance, utilizing the industry standard methodologies.</p>
      <a class="btn">Read More</a>
    </article>
    <article class="svc-card">
      <h3>Technology Assessment</h3>
      <div class="photo blue" role="img" aria-label="Photo of engineers inspecting network cabling"></div>
      <p>Experience has shown companies that perform objective, third-party technology assessments have proven…</p>
      <a class="btn">Read More</a>
    </article>
    <article class="svc-card">
      <h3>Technology Consulting</h3>
      <div class="photo" role="img" aria-label="Photo of consultants at a meeting table"></div>
      <p>Implementing quality solutions is more than applying technology to problems. You need experts with deep…</p>
      <a class="btn">Read More</a>
    </article>
  </div>
</section>

<section class="strategy">
  <div class="kicker">Our Strategy</div>
  <h2 class="section-title">YOUR PATH TO SUCCESS</h2>
  <div class="copy">
    <p>Civilian and Federal agencies are facing increased demands driven by the changing economic environment and shifts in the way products and services are sold and delivered.</p>
    <p>These factors have created an imperative to leverage new and innovative technology solution architectures like cloud computing to help reduce cost and deliver profit-driving IT capabilities faster than ever before.</p>
    <p class="lead">These are the five pillars of our successful IT strategy:</p>
  </div>
  <svg class="diagram" width="1200" height="318" viewBox="0 0 1200 318" font-family="Jost, sans-serif">
    <circle cx="599" cy="318" r="158" fill="none" stroke="#bbb" stroke-dasharray="2 3"/>
    <path d="M459 318 A140 140 0 0 1 739 318 Z" fill="#a51d36"/>
    <path d="M485 318 A114 114 0 0 1 713 318 Z" fill="#fff"/>
    <text x="599" y="288" text-anchor="middle" font-family="Montserrat, sans-serif" font-weight="800" font-size="17" fill="#231f20">Brightwave</text>
    <g fill="#fff" stroke="#888">
      <circle cx="599" cy="160" r="3.5"/><circle cx="513" cy="185" r="3.5"/><circle cx="685" cy="185" r="3.5"/><circle cx="465" cy="260" r="3.5"/><circle cx="733" cy="260" r="3.5"/>
    </g>
    <text x="599" y="13" text-anchor="middle" font-size="16" fill="#a51d36">Implement</text>
    <text x="398" y="143" text-anchor="end" font-size="16" fill="#333">Recommend</text>
    <text x="800" y="143" font-size="16" fill="#333">Monitor</text>
    <text x="330" y="266" text-anchor="end" font-size="16" fill="#333">Assess</text>
    <text x="871" y="266" font-size="16" fill="#333">Manage</text>
    <g>
      <circle cx="599" cy="80" r="41" fill="#a51d36" stroke="#fff" stroke-width="3"/><circle cx="599" cy="80" r="44" fill="none" stroke="#a51d36"/>
      <rect x="584" y="66" width="28" height="28" fill="none" stroke="#fff" stroke-width="2"/><circle cx="605" cy="70" r="5" fill="none" stroke="#fff" stroke-width="2"/>
    </g>
    <g fill="#231f20" stroke="#fff" stroke-width="3">
      <circle cx="460" cy="133" r="40"/><circle cx="739" cy="133" r="40"/><circle cx="390" cy="256" r="40"/><circle cx="809" cy="256" r="40"/>
    </g>
    <g fill="none" stroke="#231f20">
      <circle cx="460" cy="133" r="43"/><circle cx="739" cy="133" r="43"/><circle cx="390" cy="256" r="43"/><circle cx="809" cy="256" r="43"/>
    </g>
    <g fill="none" stroke="#fff" stroke-width="2">
      <circle cx="460" cy="133" r="14"/><path d="M454 136v-6h4l3-6h3v6h4v8h-10"/>
      <rect x="727" y="121" width="24" height="18"/><circle cx="741" cy="131" r="5"/><path d="M745 135l5 5"/>
      <rect x="378" y="242" width="22" height="28"/><path d="M383 250h12M383 256h12M383 262h8"/>
      <path d="M800 262a9 9 0 0 1 2-14M818 250a9 9 0 0 1-2 14"/><circle cx="812" cy="248" r="4"/>
    </g>
  </svg>
</section>

<section class="blog">
  <div class="kicker">IT News</div>
  <h2 class="section-title">LATEST FROM OUR BLOG</h2>
  <svg class="chev" style="left:82px;top:2608px;position:absolute" width="28" height="64"><path d="M26 2 4 32l22 30" fill="none" stroke="#999" stroke-width="3"/></svg>
  <svg class="chev" style="left:1090px;top:2608px;position:absolute" width="28" height="64"><path d="M2 2l22 30L2 62" fill="none" stroke="#999" stroke-width="3"/></svg>
  <div class="posts">
    <article class="post">
      <div class="photo" role="img" aria-label="Photo of colleagues working at a table with laptops"></div>
      <div class="date"><span class="d">09</span><span class="m">SEP' 19</span></div>
      <h4>Lorem Ipsum Dolor Sit Amet,<br>Consectetuer Adipiscing</h4>
      <p>Lorem ipsum dolor sit amet, consecte<br>tuer adipiscing elitd diam nonummy nibh<br>euismod tincidunt ut laoreet.</p>
      <a class="btn">Continue Reading &nbsp;→</a>
    </article>
    <article class="post">
      <div class="photo cool" role="img" aria-label="Photo of a hand using a tablet with gear graphics"></div>
      <div class="date"><span class="d">08</span><span class="m">SEP' 19</span></div>
      <h4>Lorem Ipsum Dolor Sit Amet,<br>Consectetuer Adipiscing</h4>
      <p>Lorem ipsum dolor sit amet, consecte<br>tuer adipiscing elitd diam nonummy nibh<br>euismod tincidunt ut laoreet.</p>
      <a class="btn">Continue Reading &nbsp;→</a>
    </article>
    <article class="post">
      <div class="photo screen" role="img" aria-label="Photo of presenters in front of a data wall"></div>
      <div class="date"><span class="d">07</span><span class="m">SEP' 19</span></div>
      <h4>Lorem Ipsum Dolor Sit Amet,<br>Consectetuer Adipiscing</h4>
      <p>Lorem ipsum dolor sit amet, consecte<br>tuer adipiscing elitd diam nonummy nibh<br>euismod tincidunt ut laoreet.</p>
      <a class="btn">Continue Reading &nbsp;→</a>
    </article>
  </div>
</section>

<footer class="footer">
  <svg width="1200" height="110" viewBox="0 0 1200 110" style="position:absolute;top:0;left:0">
    <path d="M0 110 L0 95 C300 20 650 60 900 60 C1050 60 1150 20 1200 0 V110Z" fill="#262626"/>
    <path d="M540 65 C800 90 1050 60 1200 0 V40 C1080 80 820 90 540 65Z" fill="#a51d36"/>
  </svg>
  <div class="footer-body">
    <div class="fcol" style="left:142px;top:42px">
      <h5>Quick Links</h5>
      <ul class="links"><li>Home</li><li>About Us</li><li>Services</li><li>Strategy</li><li>IT News</li><li>IT News</li></ul>
    </div>
    <div class="vline" style="left:332px"></div>
    <div class="fcol" style="left:408px;top:42px;width:330px">
      <h5 style="padding-right:70px">Contact Details</h5>
      <div class="contact-row" style="margin-top:16px">
        <span class="ring"><svg width="12" height="16" viewBox="0 0 12 16"><path d="M6 0a6 6 0 0 1 6 6c0 4-6 10-6 10S0 10 0 6a6 6 0 0 1 6-6z" fill="#fff"/><circle cx="6" cy="6" r="2" fill="#262626"/></svg></span>
        <div>BRIGHTWAVE PARTNERS, INC<br>2207 Larkfield Ln<br>Easton Hollow, MD 20999</div>
      </div>
      <div class="contact-row" style="margin-top:16px;align-items:center">
        <span class="ring"><svg width="14" height="14" viewBox="0 0 24 24"><path fill="#fff" d="M6.6 10.8a15 15 0 0 0 6.6 6.6l2.2-2.2a1 1 0 0 1 1-.25 11.4 11.4 0 0 0 3.6.57 1 1 0 0 1 1 1V20a1 1 0 0 1-1 1A17 17 0 0 1 3 4a1 1 0 0 1 1-1h3.5a1 1 0 0 1 1 1c0 1.25.2 2.45.57 3.57a1 1 0 0 1-.25 1z"/></svg></span>
        <div>555-013-7782</div>
      </div>
      <div class="contact-row" style="margin-top:20px;align-items:center">
        <span class="ring"><svg width="14" height="10" viewBox="0 0 16 11"><rect x=".5" y=".5" width="15" height="10" fill="none" stroke="#fff"/><path d="M.5.5 8 6l7.5-5.5" fill="none" stroke="#fff"/></svg></span>
        <div>Inquiry@brightwavepartners.example</div>
      </div>
    </div>
    <div class="vline" style="left:702px"></div>
    <div class="fcol" style="left:797px;top:36px">
      <div class="brand"><span class="mark"></span>Brightwave Partners</div>
      <p class="fabout">Brightwave Partners, Inc. is an 8(a) full-service IT consulting company based in the Washington, DC Metro area. We offer specialized, highly customized technology solutions for our customers located throughout the United States. Learn about our Services now.</p>
    </div>
  </div>
  <div class="bottombar">
    Copyright © BRIGHTWAVE PARTNERS INC. All Rights Reserved.
    <div class="socials"><span></span><span></span><span></span><span></span></div>
  </div>
</footer>

</body>
</html>
```